Web Design for Meadowfield Turf Crew

Meadowfield Turf Crew needs the photoshop files for a simple, clean and professional web design. I need a home and subpage design, although they can be very similar. See pagestridehub.com for a desired layout, although I'd like to see more design than shown on that site. The goal of the site is to attract both lawn maintenance/landscape customers and build a partner network of consultants that serve the US market. The following are needed:

- home and subpage design
- page: Home, Services, Locations, Consultants, FAQ, Contact
- if subpages have header photo, need to include 5 different header photos for each page
- favicon
Updates

I'll award the design based on the homepage concept. The minor subpage changes and other elements can be worked out in the workroom stage. Thanks, Trent

Industry/Entity Type

It Professional

```html
<!DOCTYPE html>
<html lang="en">
<head>
<meta charset="utf-8">
<title>Meadowfield Turf Crew</title>
<link href="https://fonts.googleapis.com/css2?family=Arimo:wght@400;700&display=swap" rel="stylesheet">
<style>
  :root {
    --nav-grey: #6a6a6c;
    --panel-grey: #6b6b6d;
    --caption-grey: #6e6e70;
    --green-light: #8fcf1a;
    --green: #5fae0e;
    --green-dark: #3f8f08;
    --leaf-soft: #a9d64a;
    --sky-blue: #76a3d6;
    --text-dark: #4a4a4a;
    --text-mid: #7a7a7a;
    --white: #ffffff;
    --bar-grey: #d6d6d6;
    --button-dark: #3d3d3f;
  }
  * { box-sizing: border-box; margin: 0; padding: 0; }
  html, body { width: 952px; height: 1200px; overflow: hidden; }
  body {
    position: relative;
    font-family: "Arimo", Arial, sans-serif;
    background: linear-gradient(180deg, #e7eed8 0%, #eef2e6 30%, #f2f4ee 60%, #ffffff 100%);
    color: var(--text-dark);
  }
  .abs { position: absolute; }

  /* header */
  .site-header { left: 0; top: 0; width: 952px; height: 93px;
    background: radial-gradient(ellipse at 15% 0%, #fbfdf3 0%, #e3ecd0 55%, #dbe6c8 100%); }
  .brand { left: 0; top: 30px; width: 952px; display: flex; justify-content: center; align-items: center; gap: 10px; }
  .brand-mark { width: 22px; height: 22px; border: 3px solid #6b6b6d; border-radius: 4px; }
  .brand-name { font-size: 24px; font-weight: 400; color: #6b6b6d; letter-spacing: 0.5px; }

  .main-nav { left: 0; top: 93px; width: 952px; height: 28px; background: var(--nav-grey); }
  .main-nav a { position: absolute; top: 8px; font-size: 10.5px; color: var(--white); text-decoration: none; letter-spacing: 0.6px; }
  .main-nav .sep { position: absolute; top: 9px; width: 1px; height: 10px; border-left: 1px dotted #a9a9ab; }

  /* hero */
  .hero-main { left: 75px; top: 145px; width: 360px; height: 303px; border-radius: 6px; overflow: hidden; background: var(--caption-grey); }
  .hero-main .photo { height: 233px; background: linear-gradient(180deg, #d8d6d2 0%, #c9c2b6 55%, #a9a76a 85%, #8aa33c 100%); }
  .hero-main .dots { position: absolute; left: 165px; top: 214px; display: flex; gap: 2px; }
  .hero-main .dots span { width: 8px; height: 8px; border-radius: 2px; background: var(--green); }
  .hero-main .dots span:first-child { background: var(--white); }
  .hero-main h2 { position: absolute; left: 12px; top: 246px; font-size: 17.5px; font-weight: 400; color: var(--white); line-height: 21px; }

  .tile { border-radius: 6px; overflow: hidden; }
  .tile-mower { left: 438px; top: 145px; width: 218px; height: 218px;
    background: linear-gradient(180deg, #5e8a2c 0%, #6ca43a 45%, #7cbc3a 100%); }
  .tile-meadow { left: 658px; top: 145px; width: 219px; height: 218px;
    background: linear-gradient(180deg, #4d2f2d 0%, #3c4a24 45%, #2f5b1a 100%); }
  .tile-meadow span { position: absolute; left: 0; top: 100px; width: 100%; text-align: center; font-size: 14px; color: var(--white); }
  .tile-banner { left: 438px; top: 366px; width: 439px; height: 83px;
    background: linear-gradient(90deg, #9cc0e4 0%, #7aa6d8 40%, var(--sky-blue) 100%); }
  .tile-banner .photo { position: absolute; left: 0; top: 0; width: 150px; height: 83px;
    background: linear-gradient(180deg, #a8c4e4 0%, #a8c4e4 70%, #6f9a3c 100%); }
  .tile-banner span { position: absolute; right: 16px; top: 28px; font-size: 22px; color: var(--white); }

  /* service buttons */
  .service { height: 48px; }
  .service .pill { position: absolute; left: 0; top: 0; height: 48px; border-radius: 24px;
    background: linear-gradient(180deg, var(--green-light) 0%, #6cbc12 50%, var(--green) 100%);
    box-shadow: 0 3px 4px rgba(0,0,0,0.25); }
  .service .pill span { position: absolute; top: 13px; font-size: 20px; font-weight: 700; color: var(--white);
    text-shadow: 0 1px 2px rgba(0,0,0,0.35); }
  .service .accent { position: absolute; top: -14px; width: 50px; height: 64px; border-radius: 6px;
    background: linear-gradient(180deg, var(--leaf-soft) 0%, var(--green) 100%); opacity: 0.85; }

  /* content band */
  .content-band { left: 0; top: 614px; width: 952px; height: 292px; background: var(--panel-grey); border-top: 3px solid #67b81c; }
  .content-band h1 { position: absolute; left: 77px; top: 42px; font-size: 29px; font-weight: 700; color: var(--white); }
  .content-band p { position: absolute; left: 77px; width: 486px; font-size: 10.6px; line-height: 13.6px;
    letter-spacing: 0.4px; color: var(--white); }
  .content-band p strong { font-size: 12px; font-weight: 400; letter-spacing: 0.3px; }

  .contact-card { left: 592px; top: 672px; width: 279px; height: 252px; border-radius: 6px;
    background: linear-gradient(180deg, #8ccc12 0%, #6cb812 50%, #4ea40c 100%); }
  .contact-card h3 { position: absolute; left: 0; top: 18px; width: 100%; text-align: center; font-size: 26px; font-weight: 700; color: var(--white); }
  .contact-card .rule { position: absolute; left: 10px; top: 50px; width: 259px; height: 4px;
    border-top: 1px solid #d8f08a; border-bottom: 1px solid #d8f08a; }
  .contact-card .field { position: absolute; left: 32px; width: 216px; height: 31px; border: 1px solid #dff29e; border-radius: 2px;
    font-size: 10.5px; color: var(--white); padding: 9px 14px; }
  .contact-card .submit { position: absolute; left: 33px; top: 198px; width: 214px; height: 36px; border-radius: 3px;
    background: linear-gradient(180deg, #4b4b4d 0%, var(--button-dark) 100%); box-shadow: 0 2px 3px rgba(0,0,0,0.35);
    text-align: center; font-size: 17px; font-weight: 700; color: var(--white); line-height: 36px; }
  .card-accent { left: 860px; top: 626px; width: 40px; height: 58px; border-radius: 6px;
    background: linear-gradient(180deg, var(--leaf-soft) 0%, var(--green) 100%); opacity: 0.85; }

  .lawn-strip { left: 0; top: 906px; width: 952px; height: 68px; background: #fbfbfb; border-bottom: 2px solid #8cc63f; }
  .mower-figure { left: 868px; top: 922px; width: 72px; height: 52px; border-radius: 4px;
    background: linear-gradient(180deg, #eeeeee 0%, #d6d6d6 100%); }

  /* footer */
  .social { top: 1000px; width: 32px; height: 32px; border-radius: 50%; }
  .footer-nav a { position: absolute; top: 1011px; font-size: 9px; color: var(--text-mid); text-decoration: none; letter-spacing: 0.3px; }
  .copyright { left: 76px; top: 1059px; width: 800px; height: 39px; background: var(--bar-grey);
    font-size: 10px; color: var(--text-dark); padding: 13px 20px; }
  .footer-brand { left: 0; top: 1131px; width: 952px; display: flex; justify-content: center; align-items: center; gap: 8px; }
  .footer-brand .brand-mark { width: 18px; height: 18px; border: 2px solid #9a9a9a; }
  .footer-brand .brand-name { font-size: 19px; color: #9a9a9a; }
  .legal-links { left: 0; top: 1175px; width: 952px; text-align: center; font-size: 10px; color: var(--text-dark); letter-spacing: 0.4px; }
  .legal-links span.dot { margin: 0 12px; }
</style>
</head>
<body>

<header class="abs site-header">
  <div class="abs brand">
    <span class="brand-mark"></span>
    <span class="brand-name">Meadowfield Turf Crew</span>
  </div>
</header>

<nav class="abs main-nav">
  <a style="left:202px">HOME</a><span class="sep" style="left:255px"></span>
  <a style="left:279px">SERVICES</a><span class="sep" style="left:357px"></span>
  <a style="left:379px">LOCATIONS</a><span class="sep" style="left:468px"></span>
  <a style="left:491px">CONSULTANTS</a><span class="sep" style="left:598px"></span>
  <a style="left:624px">FAQ</a><span class="sep" style="left:668px"></span>
  <a style="left:688px">CONTACT</a>
</nav>

<section class="abs hero-main">
  <div class="photo" role="img" aria-label="Photo: gardener trimming grass with shears"></div>
  <div class="dots"><span></span><span></span><span></span></div>
  <h2>UT WISI ENIM AD MINIM VENIAM, QUIS<br>NOSTRUD EXERCI TATION</h2>
</section>

<div class="abs tile tile-mower" role="img" aria-label="Photo: man pushing a green lawn mower across a backyard lawn"></div>
<div class="abs tile tile-meadow" role="img" aria-label="Photo: lawn mower among daisies in tall grass"><span>Dignissim Qui Blandit</span></div>
<div class="abs tile tile-banner">
  <div class="photo" role="img" aria-label="Photo: red lawn mower on grass under a blue sky"></div>
  <span>Sed Diam Nonummy Nibh</span>
</div>

<div class="abs service" style="left:75px; top:516px; width:260px;">
  <div class="pill" style="width:208px"><span style="left:24px">MAINTENANCE</span></div>
  <div class="accent" style="left:206px" role="img" aria-label="Leaf ornament"></div>
</div>
<div class="abs service" style="left:347px; top:516px; width:260px;">
  <div class="pill" style="width:206px"><span style="left:44px">FERTILIZER</span></div>
  <div class="accent" style="left:204px" role="img" aria-label="Leaf ornament"></div>
</div>
<div class="abs service" style="left:622px; top:516px; width:260px;">
  <div class="pill" style="width:206px"><span style="left:30px">PEST CONTROL</span></div>
  <div class="accent" style="left:205px" role="img" aria-label="Leaf ornament"></div>
</div>

<section class="abs content-band">
  <h1>Ut wisi enim ad minim veniam</h1>
  <p style="top:84px">Lorem ipsum dolor sit amet, consectetuer adipiscing elit, sed diam nonummy nibh euismod tincidunt ut laoreet dolore magna aliquam erat volutpat. Ut wisi enim ad minim veniam, quis nostrud exerci tation ullamcorper suscipit lobortis nisl ut aliquip ex ea commodo consequat. Duis autem vel eum iriure dolor in hendrerit in vulputate velit esse molestie consequat, vel illum dolore eu feugiat nulla facilisis at vero eros et accumsan et iusto odio dignissim qui blandit praesent luptatum zzril delenit augue duis dolore te feugait nulla facilisi.</p>
  <p style="top:173px"><strong>Consectetuer adipiscing elit</strong>, sed diam nonummy nibh euismod tincidunt ut laoreet dolore magna aliquam erat volutpat. Ut wisi enim ad minim veniam, quis nostrud exerci tation ullamcorper suscipit lobortis nisl ut aliquip ex ea commodo consequat. Duis autem vel eum iriure dolor in hendrerit in vulputate.</p>
</section>

<div class="abs lawn-strip"></div>
<div class="abs mower-figure" role="img" aria-label="Illustration: person mowing the lawn"></div>

<form class="abs contact-card">
  <h3>CONTACT US</h3>
  <div class="rule"></div>
  <div class="field" style="top:74px">NAME</div>
  <div class="field" style="top:114px">LAST NAME</div>
  <div class="field" style="top:154px">E-MAIL ADDRESS</div>
  <div class="submit">SUBMIT NOW</div>
</form>
<div class="abs card-accent" role="img" aria-label="Leaf ornament"></div>

<div class="abs social" style="left:78px; background:#3b5a9a"></div>
<div class="abs social" style="left:114px; background:#3aa3dc"></div>
<div class="abs social" style="left:150px; background:#1f6ea3"></div>
<div class="abs social" style="left:186px; background:#dc4e41"></div>

<nav class="footer-nav">
  <a style="left:428px">HOME</a>
  <a style="left:493px">SERVICES</a>
  <a style="left:578px">LOCATIONS</a>
  <a style="left:669px">CONSULTANTS</a>
  <a style="left:774px">FAQ</a>
  <a style="left:831px">CONTACT</a>
</nav>

<div class="abs copyright">© 2014 Meadowfield Turf Crew.com,</div>

<div class="abs footer-brand">
  <span class="brand-mark"></span>
  <span class="brand-name">Meadowfield Turf Crew</span>
</div>

<div class="abs legal-links">
  LEGAL<span class="dot">.</span>PRIVACY POLICY<span class="dot">.</span>CONSUMER ACCESS<span class="dot">.</span>EMPLOYMENT OPPORTUNITY
</div>

</body>
</html>
```